Faltblatt Hausmeisterei
Zielgruppe
Ich benötige einen neuen Flyer für eine Hausmeisterei http://www.objektpflege-kernwald.de/.
Zielgruppe ist hier nicht nur der Privathaushalt mit Renovierungen oder Reparaturen sondern auch eine Firma oder Kanzlei oder Hausverwaltung welche eine Objektbetreuung vergibt.
Es soll wieder ein beidseitiger Faltblattflyer werden. Hinsichtlich Farbe und Design Inhalt bin ich jedoch offen.
Aufgabenstellung
Ich habe unseren alten Faltblattflyer angefügt der Flyer sollte in diese Richtung gehen jedoch etwas moderner sein.

```html
<!DOCTYPE html>
<html lang="de">
<head>
<meta charset="utf-8">
<title>Kernwald Hausmeisterei – Faltblatt</title>
<link rel="stylesheet" href="https://fonts.googleapis.com/css2?family=Archivo:wght@600;700;800&family=Inter:wght@300;400&display=swap">
<style>
  :root {
    --green: #7ea827;
    --green-dark: #6b9320;
    --yellow: #f9cf0c;
    --ink: #111111;
    --text: #1e1e1e;
    --white: #ffffff;
    --page: #ffffff;
  }
  * { margin: 0; padding: 0; box-sizing: border-box; }
  html, body { width: 1200px; height: 1175px; overflow: hidden; background: var(--page); }
  body { position: relative; font-family: "Inter", Helvetica, Arial, sans-serif; color: var(--text); }

  .panel {
    position: absolute; top: 71px; width: 479px; height: 1015px;
    overflow: hidden; background: var(--white);
    box-shadow: 0 6px 28px rgba(0,0,0,.22);
  }
  .panel--front { left: 84px; }
  .panel--back { left: 640px; }

  .panel__shapes { position: absolute; inset: 0; }

  /* Front */
  .brand { position: absolute; left: 39px; top: 25px; display: flex; align-items: center; gap: 24px; }
  .brand__square { width: 114px; height: 62px; background: var(--white); border-radius: 2px; }
  .brand__name { font-family: "Archivo", Helvetica, Arial, sans-serif; font-weight: 800; font-size: 46px; color: var(--white); line-height: 1; letter-spacing: 1px; }
  .brand__tagline { position: absolute; left: 176px; top: 70px; font-size: 12.5px; color: var(--white); white-space: nowrap; font-weight: 400; }

  .callout {
    position: absolute; background: var(--yellow);
    border-radius: 48px 0 0 48px; transform: rotate(-2.2deg);
    font-family: "Archivo", Helvetica, Arial, sans-serif; font-weight: 700; color: var(--ink);
  }
  .callout__line { display: block; line-height: 1.12; }
  .callout__line--lead { font-weight: 800; }
  .panel--front .callout { left: 169px; top: 626px; width: 340px; height: 116px; padding: 20px 0 0 49px; font-size: 24px; }
  .panel--back .callout { left: 246px; top: 816px; width: 260px; height: 100px; padding: 18px 0 0 37px; font-size: 19.5px; }

  .front-intro { position: absolute; left: 39px; top: 777px; color: var(--white); }
  .front-intro__title { font-family: "Archivo", Helvetica, Arial, sans-serif; font-weight: 700; font-size: 21.5px; line-height: 1.27; letter-spacing: .2px; }
  .front-intro__list { list-style: none; margin-top: 8px; }
  .front-intro__list li { font-size: 22.5px; font-weight: 300; line-height: 29px; padding-left: 22px; position: relative; }
  .front-intro__list li::before { content: ""; position: absolute; left: 2px; top: 12px; width: 8px; height: 8px; border-radius: 50%; background: var(--white); }

  .footer-bar { position: absolute; left: 0; right: 0; bottom: 0; height: 56px; background: var(--yellow); display: flex; align-items: center; justify-content: center; }
  .footer-bar__url { font-family: "Archivo", Helvetica, Arial, sans-serif; font-weight: 700; font-size: 21px; color: var(--ink); }
  .panel--back .footer-bar { height: 57px; }

  /* Back */
  .back-header { position: absolute; left: 0; right: 0; top: 0; height: 53px; background: var(--green); display: flex; align-items: center; justify-content: center; }
  .back-header__title { font-family: "Archivo", Helvetica, Arial, sans-serif; font-weight: 700; font-size: 24px; color: var(--white); letter-spacing: .5px; }

  .service-photo { position: absolute; left: 0; width: 223px; height: 199px; }
  .service-photo--caretaker { top: 53px; background: linear-gradient(135deg, #8a9cb0 0%, #4f6a86 45%, #9a6a3a 75%, #3b3b40 100%); }
  .service-photo--garden { top: 256px; background: linear-gradient(120deg, #3e6b26 0%, #6e9a3c 45%, #2f6b4c 75%, #d56a2a 100%); }
  .service-photo--clearance { top: 457px; background: linear-gradient(130deg, #a45a3c 0%, #c9b99a 45%, #8c5a3a 70%, #d9d2c0 100%); }
  .service-photo--renovation { top: 658px; height: 199px; background: linear-gradient(160deg, #f1f1ee 0%, #e2dcd2 50%, #d0a86d 100%); }

  .service { position: absolute; left: 241px; width: 230px; }
  .service__title { font-family: "Archivo", Helvetica, Arial, sans-serif; font-weight: 700; font-size: 17px; line-height: 21px; color: var(--green); margin-bottom: 5px; }
  .service__list { list-style: none; }
  .service__list li { position: relative; padding-left: 12px; font-size: 15.5px; line-height: 20.5px; margin-bottom: 3.5px; font-weight: 400; color: var(--text); }
  .service__list li::before { content: ""; position: absolute; left: 1px; top: 8px; width: 5px; height: 5px; border-radius: 50%; background: var(--ink); }
  .service__list li.service__note { font-size: 12.5px; line-height: 17px; }
  .service__list li.service__note::before { top: 5px; }

  .service--caretaker { top: 71px; }
  .service--garden { top: 268px; }
  .service--clearance { top: 471px; }
  .service--renovation { top: 674px; }

  .contact-area { position: absolute; left: 0; right: 0; top: 857px; height: 101px; background: var(--green); }
  .contact { position: absolute; left: 39px; top: 868px; color: var(--white); font-size: 15.5px; line-height: 20.5px; font-weight: 300; }
  .contact__name { font-family: "Archivo", Helvetica, Arial, sans-serif; font-weight: 700; font-size: 16.5px; }
</style>
</head>
<body>

<section class="panel panel--front" aria-label="Titelseite">
  <svg class="panel__shapes" width="479" height="1015" viewBox="0 0 479 1015" aria-hidden="true">
    <path d="M0 0 H479 V108 Q230 105 0 146 Z" fill="var(--green)"/>
  </svg>
  <div role="img" aria-label="Foto: lächelnder Handwerker in Latzhose zeigt Daumen hoch" style="position:absolute;left:0;top:120px;width:479px;height:600px;background:linear-gradient(160deg,#d9d6d1 0%,#c7beb2 35%,#4f79a8 60%,#2b3c55 100%);clip-path:polygon(0 33px,100% 0,100% 100%,0 100%);"></div>
  <svg class="panel__shapes" width="479" height="1015" viewBox="0 0 479 1015" aria-hidden="true">
    <path d="M0 146 Q230 105 479 108" fill="none" stroke="var(--white)" stroke-width="6"/>
    <path d="M0 712 Q220 716 479 700 V1015 H0 Z" fill="var(--green)"/>
    <path d="M0 710 Q220 714 479 698" fill="none" stroke="var(--white)" stroke-width="5"/>
  </svg>

  <div class="brand">
    <span class="brand__square" aria-hidden="true"></span>
    <span class="brand__name">KERNWALD</span>
  </div>
  <p class="brand__tagline">Ihr engagierter Familien-Handwerksbetrieb!</p>

  <div class="callout">
    <span class="callout__line callout__line--lead">JETZT ANRUFEN!</span>
    <span class="callout__line">Sofort-Beratung</span>
    <span class="callout__line">0170 - 555 42 19</span>
  </div>

  <div class="front-intro">
    <h1 class="front-intro__title">IHR ENGAGIERTER HAUSMEISTER-<br>FAMILIENBETRIEB IN MÜNCHEN</h1>
    <ul class="front-intro__list">
      <li>Hausmeisterservice + mehr</li>
      <li>Garten- &amp; Beetpflege</li>
      <li>Renovierungen</li>
      <li>Entrümpelungen + mehr</li>
    </ul>
  </div>

  <div class="footer-bar"><span class="footer-bar__url">www.objektpflege-kernwald.de</span></div>
</section>

<section class="panel panel--back" aria-label="Leistungen">
  <header class="back-header"><h2 class="back-header__title">UNSERE LEISTUNGEN</h2></header>

  <div class="service-photo service-photo--caretaker" role="img" aria-label="Foto: Handwerker mit Werkzeuggürtel und Klemmbrett"></div>
  <div class="service-photo service-photo--garden" role="img" aria-label="Foto: Heckenschnitt mit elektrischer Heckenschere"></div>
  <div class="service-photo service-photo--clearance" role="img" aria-label="Foto: Sperrmüll vor Backsteinwand mit Schild zur Entrümpelung"></div>
  <div class="service-photo service-photo--renovation" role="img" aria-label="Foto: Handwerker verlegt Parkettboden"></div>

  <div class="service service--caretaker">
    <h3 class="service__title">HAUSMEISTERSERVICE<br>+ MEHR</h3>
    <ul class="service__list">
      <li>Hausmeisterservice,</li>
      <li>Reparaturdienste</li>
      <li>Renovierungen</li>
      <li class="service__note">seit über 15 Jahren zuverlässiger Partner vor Ort für Vermieter, Hauseigentümer/-verwaltungen &amp; Behörden</li>
    </ul>
  </div>

  <div class="service service--garden">
    <h3 class="service__title">GARTEN- &amp; BEETPFLEGE</h3>
    <ul class="service__list">
      <li>Rasenpflege, Düngen, Wässern, Vertikutieren</li>
      <li>Heckenschneiden</li>
      <li>Bäume fällen</li>
      <li>Laub abräumen, Dachrinnen-Reinigung</li>
      <li>Pflasterarbeiten</li>
    </ul>
  </div>

  <div class="service service--clearance">
    <h3 class="service__title">ENTRÜMPELUNGEN<br>+ MEHR</h3>
    <ul class="service__list">
      <li>Keller-, Wohnungs- &amp; Büroauflösungen</li>
      <li>kurzfristig &amp; zum fairen Preis</li>
      <li class="service__note">seit fast 20 Jahren zuverlässiger Partner vor Ort für Vermieter, Hauseigentümer/-verwalter &amp; Behörden</li>
    </ul>
  </div>

  <div class="service service--renovation">
    <h3 class="service__title">RENOVIERUNGEN</h3>
    <ul class="service__list">
      <li>Malern, Türen und Heizkörper lackieren</li>
      <li>Teppich/Laminat verlegen</li>
      <li>Reparaturdienste, Umzugs-hilfe &amp; Entrümpelungen</li>
    </ul>
  </div>

  <div class="contact-area"></div>
  <address class="contact" style="font-style:normal">
    <span class="contact__name">Hausmeisterei Kernwald</span><br>
    Lindenhofer Str. 9<br>
    80999 München<br>
    service@objektpflege-kernwald.de
  </address>

  <div class="callout">
    <span class="callout__line callout__line--lead">JETZT ANRUFEN!</span>
    <span class="callout__line">Sofort-Beratung</span>
    <span class="callout__line">0170 - 555 42 19</span>
  </div>

  <div class="footer-bar"><span class="footer-bar__url">www.objektpflege-kernwald.de</span></div>
</section>

</body>
</html>
```